Reaching the Right Campus Might Be Simpler Than Expected! Nine Moves Toward Stronger Report Cards...

I need a cover/front/spine/back for an e-book and a hard cover book that I am publishing on Zembrix. I have written a book with an eight step process on how to help parents coach their kids to getting grades up and accepted into good colleges. In the book, I am highlighting current day struggles teens and young adults are having with mental health due to the impact of social media. I am helping them understand the impact mental health and social media has had on school stress. I outline a process in my book that my reader can implement herself with her child, or hire me as her coach.

Target Market(s)

Women ages 35 to 55 with teens in high school and college

Industry/Entity Type

Life Coaching

Font styles to use
Serif

Colors

Designer to choose colors to be used in the design.

Requirements
Must have
• Title, name, (credentials/PhD) and simple image on cover. Font and
• point size that you can read in a teeny, tiny thumbnail. Readability is number one goal. Text on thumbnail must be readable. I have been made aware that subtitles are hard to get on E-books.
Nice to have
• Something that immediately lets the reader know what my book is about
Should not have
• No italics or swirly curly font.

```html
<!DOCTYPE html>
<html lang="en">
<head>
<meta charset="utf-8">
<title>Reaching the Right Campus – Book Cover</title>
<link rel="stylesheet" href="https://fonts.googleapis.com/css2?family=Anton&family=Josefin+Sans:wght@300;400;600;700&display=swap">
<style>
  :root {
    --page: #ffffff;
    --band: #fcc96e;
    --blue-deep: #0b74d1;
    --blue-mid: #1a9be6;
    --blue-glow: #2fd3f0;
    --white: #ffffff;
    --banner: #ededee;
    --banner-shade: #d6d7d9;
    --ink: #4a4a4c;
    --ink-strong: #3a3a3c;
  }
  * { box-sizing: border-box; margin: 0; padding: 0; }
  html, body { width: 1200px; height: 1200px; overflow: hidden; background: var(--page); }
  .canvas { position: relative; width: 1200px; height: 1200px; }
  .cover {
    position: absolute; left: 255px; top: 40px; width: 690px; height: 1120px;
    background: radial-gradient(ellipse 60% 45% at 50% 55%, var(--blue-glow) 0%, var(--blue-mid) 55%, var(--blue-deep) 100%);
    overflow: hidden;
    font-family: "Josefin Sans", sans-serif;
    color: var(--white);
  }
  .author-band {
    height: 96px; background: var(--band);
    display: flex; align-items: center; justify-content: center;
    font-size: 40px; letter-spacing: 6px; padding-top: 8px;
  }
  .author-name { font-weight: 700; }
  .author-credential { font-weight: 300; margin-left: 14px; }
  .title-lead {
    margin-top: 28px; text-align: center;
    font-weight: 300; font-size: 70px; letter-spacing: 3px; line-height: 1;
  }
  .title-main {
    margin-top: 14px; text-align: center;
    font-family: "Anton", sans-serif; font-size: 116px; line-height: 1.05; letter-spacing: 0;
  }
  .subtitle-banner {
    position: relative; margin: 14px 60px 0 30px; height: 150px;
    background: linear-gradient(180deg, var(--banner) 0%, #f4f4f5 50%, var(--banner-shade) 100%);
    display: flex; flex-direction: column; align-items: center; justify-content: center;
    color: var(--ink); font-size: 42px; letter-spacing: 1.5px; line-height: 1.25; font-weight: 400;
    clip-path: polygon(0 4%, 100% 0, 100% 100%, 0 96%);
  }
  .subtitle-banner strong { font-weight: 700; color: var(--ink-strong); }
  .banner-curl { position: absolute; right: 28px; top: 416px; }
  .cover-art {
    position: absolute; left: 175px; top: 515px; width: 340px; height: 480px;
    border-radius: 48% 48% 40% 40%;
    background: radial-gradient(ellipse at 50% 45%, rgba(255,255,255,0.55) 0%, rgba(200,235,245,0.35) 45%, rgba(40,60,80,0.15) 100%);
  }
  .tagline {
    position: absolute; left: 0; right: 0; bottom: 28px; text-align: center;
    font-size: 32px; line-height: 1.3; letter-spacing: 1.5px; font-weight: 400;
  }
  .tagline strong { font-weight: 700; letter-spacing: 2px; }
</style>
</head>
<body>
<div class="canvas">
  <div class="cover">
    <div class="author-band">
      <span class="author-name">MARTIN CALLOWAY</span><span class="author-credential">PHD</span>
    </div>
    <h1>
      <div class="title-lead">REACHING THE</div>
      <div class="title-main">RIGHT CAMPUS</div>
    </h1>
    <div class="subtitle-banner">
      <div>MIGHT BE <strong>SIMPLER</strong> THAN</div>
      <div>EXPECTED</div>
    </div>
    <svg class="banner-curl" width="60" height="160" viewBox="0 0 60 160" aria-hidden="true">
      <path d="M10 4 C40 0 58 12 52 30 L58 156 L18 150 Z" fill="#e4e5e7"/>
      <path d="M10 4 C40 0 58 12 52 30 C40 26 26 24 18 30 Z" fill="#c9cacc"/>
    </svg>
    <div class="cover-art" role="img" aria-label="Illustration of a glowing light bulb wearing a black graduation cap with a gold tassel"></div>
    <p class="tagline">
      A <strong>NINE STEP GUIDE</strong> for parents<br>
      to help kids get stronger report cards<br>
      and accepted into the <strong>RIGHT CAMPUS</strong>
    </p>
  </div>
</div>
</body>
</html>
```